Vardena General Painting Ltd. - Construction painting company providing high-quality service

We need a logo and business card design for a painting company that provides high-quality work for major developers and builders in Calgary, Alberta. Our projects include commercial high-rise residential towers. We would like designs that communicate professionalism and high quality service.
Updates
Need extra days to review
Target Market(s)
Developers and builders
Industry/Entity Type
Construction
Contact Information for Business Card
Company name, employee name, title, phone number, email address
Font styles to use
Colors
Designer to choose colors to be used in the design.
Look and feel
Each slider illustrates characteristics of the customer's brand and the style your logo design should communicate.

```html
<!DOCTYPE html>
<html lang="en">
<head>
<meta charset="utf-8">
<title>Vardena General Painting Ltd. – Business Card</title>
<link rel="stylesheet" href="https://fonts.googleapis.com/css2?family=Lato:wght@400;700&display=swap">
<style>
  :root {
    --page-bg: #e6e6e6;
    --brand-blue: #29a9e1;
    --brand-grey: #595959;
    --text-light: #ffffff;
    --seal-light: #fbfbfb;
    --seal-mid: #e4e1e1;
    --seal-edge: #cfcaca;
    --seal-text: #4f4f4f;
  }
  * { margin: 0; padding: 0; box-sizing: border-box; }
  html, body {
    width: 1200px;
    height: 900px;
    overflow: hidden;
    background: var(--page-bg);
    font-family: "Lato", sans-serif;
  }
  .business-card {
    position: absolute;
    left: 100px;
    top: 141px;
    width: 1000px;
    height: 617px;
    background: var(--brand-blue);
    overflow: hidden;
    box-shadow: 0 10px 30px rgba(0,0,0,0.15);
  }
  .grey-band {
    position: absolute;
    left: 678px;
    top: 0;
    width: 322px;
    height: 100%;
    background: var(--brand-grey);
  }
  .identity {
    position: absolute;
    left: 59px;
    top: 150px;
    color: var(--text-light);
  }
  .identity .person-name {
    font-weight: 700;
    font-size: 39px;
    line-height: 1.05;
    letter-spacing: 0.2px;
  }
  .identity .person-title {
    font-weight: 400;
    font-size: 28px;
    line-height: 1.2;
  }
  .contact-list {
    position: absolute;
    left: 59px;
    top: 347px;
    list-style: none;
    color: var(--text-light);
    font-size: 28px;
    font-weight: 400;
  }
  .contact-list li {
    display: flex;
    align-items: center;
    height: 39px;
  }
  .contact-list svg {
    width: 30px;
    height: 30px;
    margin-right: 10px;
    flex: none;
  }
  .company-seal {
    position: absolute;
    left: 412px;
    top: 41px;
    width: 532px;
    height: 532px;
    border-radius: 50%;
    background: radial-gradient(circle at 45% 40%, var(--seal-light) 0%, var(--seal-mid) 65%, var(--seal-edge) 100%);
    display: flex;
    align-items: center;
    justify-content: center;
    text-align: center;
  }
  .company-name {
    width: 360px;
    color: var(--seal-text);
    font-weight: 700;
    font-size: 40px;
    line-height: 1.25;
    letter-spacing: 1px;
  }
</style>
</head>
<body>
  <div class="business-card">
    <div class="grey-band"></div>

    <div class="identity">
      <p class="person-name">MARCUS HALE</p>
      <p class="person-title">Managing Director</p>
    </div>

    <ul class="contact-list">
      <li>
        <svg viewBox="0 0 24 24" fill="none" stroke="#fff" stroke-width="2" stroke-linecap="round" stroke-linejoin="round" aria-hidden="true">
          <path d="M5 3h4l2 5-2.5 1.5a11 11 0 0 0 6 6L16 13l5 2v4a2 2 0 0 1-2 2A16 16 0 0 1 3 5a2 2 0 0 1 2-2z"/>
          <path d="M14 3a7 7 0 0 1 7 7"/><path d="M14 7a3 3 0 0 1 3 3"/>
        </svg>
        044-987 210 365
      </li>
      <li>
        <svg viewBox="0 0 24 24" aria-hidden="true">
          <rect x="1" y="4" width="22" height="16" fill="#fff"/>
          <path d="M1 4l11 9 11-9M1 20l8-8M23 20l-8-8" fill="none" stroke="#29a9e1" stroke-width="1.6"/>
        </svg>
        info@vardenapainting.com
      </li>
      <li>
        <svg viewBox="0 0 24 24" fill="none" stroke="#fff" stroke-width="1.6" aria-hidden="true">
          <circle cx="12" cy="12" r="10"/>
          <ellipse cx="12" cy="12" rx="4.5" ry="10"/>
          <path d="M2 12h20M4 7h16M4 17h16M12 2v20"/>
        </svg>
        www.vardenapainting.com
      </li>
    </ul>

    <div class="company-seal">
      <p class="company-name">VARDENA GENERAL PAINTING LTD.</p>
    </div>
  </div>
</body>
</html>
```